Make it cool to work near where you are...

Calling all creatives - create the ultimate cool card for people who want to cut their commute.

Here at FarlowBench we've got what can best be described as an Quillet card for desks - and we want to brighten up the wallets of our most loyal users.

So, pitch us your ideas and you might see your design on cards being flashed across the country - and we've thrown in a bit of cash too.

Do see our brief card guidelines - with a couple of past examples thrown in.

```html
<!DOCTYPE html>
<html lang="en">
<head>
<meta charset="utf-8">
<title>FarlowBench Business Card</title>
<link href="https://fonts.googleapis.com/css2?family=Lato:wght@400;700;900&display=swap" rel="stylesheet">
<style>
  :root {
    --stage: #e9e7e4;
    --card-dark: #3a3a3c;
    --card-dark-edge: #2a2a2b;
    --card-light: #ffffff;
    --pink: #ef5fbf;
    --text-light: #f2f2f2;
    --text-muted: #d6d6d6;
    --ink: #4a4a4c;
  }
  * { box-sizing: border-box; margin: 0; padding: 0; }
  html, body {
    width: 1200px; height: 900px; overflow: hidden;
    background: var(--stage);
    font-family: "Lato", Arial, sans-serif;
  }
  .canvas { position: relative; width: 1200px; height: 900px; }

  .card {
    position: absolute;
    width: 525px; height: 300px;
    border-radius: 22px;
    overflow: hidden;
    box-shadow: 0 12px 30px rgba(0,0,0,0.25);
  }

  /* Front */
  .card-front {
    left: 70px; top: 110px;
    background: radial-gradient(ellipse at 55% 40%, #5a5a5c 0%, var(--card-dark) 45%, var(--card-dark-edge) 100%);
  }
  .front-brand {
    position: absolute; left: 0; right: 0; top: 104px;
    display: flex; align-items: center; justify-content: center; gap: 14px;
  }
  .brand-square {
    width: 30px; height: 30px; background: var(--pink);
  }
  .front-wordmark {
    font-weight: 900; font-size: 54px; color: var(--text-light);
    letter-spacing: -1px;
  }
  .front-web {
    position: absolute; left: 0; right: 0; top: 232px;
    text-align: center; font-weight: 700; font-size: 17px; color: var(--text-light);
  }
  .front-web .accent { color: var(--pink); }

  /* Back */
  .card-back {
    left: 605px; top: 490px;
    background: var(--card-dark);
  }
  .back-shape { position: absolute; inset: 0; }
  .back-brand {
    position: absolute; left: 34px; top: 134px;
    font-weight: 900; font-size: 30px; color: var(--pink);
    letter-spacing: -0.5px;
  }
  .contact {
    position: absolute; left: 318px; top: 30px; width: 200px;
    color: var(--text-muted); font-size: 12px; line-height: 1.35;
  }
  .contact-name { color: var(--pink); font-weight: 700; font-size: 14px; }
  .contact-title { color: var(--text-light); margin-bottom: 22px; }
  .contact-address { margin-bottom: 24px; }
  .contact-list { list-style: none; }
  .contact-list li { display: flex; align-items: center; gap: 8px; margin-bottom: 3px; }
  .contact-icon { width: 13px; height: 13px; flex: none; }
</style>
</head>
<body>
<main class="canvas">

  <section class="card card-front" aria-label="Card front">
    <div class="front-brand">
      <span class="brand-square"></span>
      <span class="front-wordmark">FarlowBench</span>
    </div>
    <p class="front-web">www.<span class="accent">farlowbench</span>.com</p>
  </section>

  <section class="card card-back" aria-label="Card back">
    <svg class="back-shape" viewBox="0 0 525 300" preserveAspectRatio="none" aria-hidden="true">
      <path d="M0 0 H262 Q300 150 292 300 H0 Z" fill="var(--card-light)"/>
      <path d="M262 0 Q300 150 292 300" fill="none" stroke="var(--pink)" stroke-width="6"/>
    </svg>

    <p class="back-brand">FarlowBench</p>

    <div class="contact">
      <p class="contact-name">Jamie Rowe</p>
      <p class="contact-title">Managing Director</p>
      <p class="contact-address">WorkHarbour, 48-52 Calder Row<br>E2 7QB London, United Kingdom</p>
      <ul class="contact-list">
        <li>
          <svg class="contact-icon" viewBox="0 0 14 14" aria-hidden="true"><path d="M3 1 L5 1 L6 4 L4.5 5.2 Q6 8 8.8 9.5 L10 8 L13 9 L13 11 Q12 13 10 13 Q2 11 1 3 Q1 1 3 1 Z" fill="var(--pink)"/></svg>
          <span>+44 20 7555 0148</span>
        </li>
        <li>
          <svg class="contact-icon" viewBox="0 0 14 14" aria-hidden="true"><rect x="1" y="3" width="12" height="9" rx="1" fill="var(--pink)"/><path d="M1.5 3.5 L7 8 L12.5 3.5" fill="none" stroke="var(--card-dark)" stroke-width="1.2"/></svg>
          <span>team@farlowbench.com</span>
        </li>
        <li>
          <svg class="contact-icon" viewBox="0 0 14 14" aria-hidden="true"><circle cx="7" cy="7" r="6" fill="var(--pink)"/><path d="M1 7 H13 M7 1 Q3 7 7 13 M7 1 Q11 7 7 13" fill="none" stroke="var(--card-dark)" stroke-width="0.9"/></svg>
          <span>www.farlowbench.com</span>
        </li>
      </ul>
    </div>
  </section>

</main>
</body>
</html>
```